Letterhead for new real estate company in South Africa named Lofthaven

A letterhead with the directors and company details to be editable as these changes often

Target Market(s)

In line with our logo brief and our newly designed logo and corporate fee

Industry/Entity Type

Real Estate

Requirements
Must have
• Details as per the sample letterhead provided.

```html
<!DOCTYPE html>
<html lang="en">
<head>
<meta charset="utf-8">
<title>Lofthaven Letterhead</title>
<link href="https://fonts.googleapis.com/css2?family=Poppins:ital,wght@0,400;0,500;1,400&display=swap" rel="stylesheet">
<style>
  :root {
    --backdrop: #e4e4e4;
    --paper: #f0f0f0;
    --paper-edge: #e2e2e2;
    --brand-green: #3fb27a;
    --earth-brown: #726556;
    --ink: #2b2b2b;
    --footer-ink: #ffffff;
    --watermark: rgba(160, 160, 160, 0.14);
  }
  * { box-sizing: border-box; margin: 0; padding: 0; }
  html, body {
    width: 960px; height: 1200px; overflow: hidden;
    background: var(--backdrop);
    font-family: "Poppins", sans-serif;
  }
  .letterhead {
    position: absolute; left: 52px; top: 0;
    width: 855px; height: 1200px;
    background: linear-gradient(90deg, var(--paper) 0%, var(--paper-edge) 100%);
  }
  .brand {
    position: absolute; left: 78px; top: 80px;
    display: flex; align-items: center; gap: 10px;
  }
  .brand-dot {
    width: 14px; height: 14px; border-radius: 50%;
    background: var(--brand-green);
  }
  .brand-name {
    font-size: 28px; font-weight: 400; letter-spacing: -0.3px;
    color: var(--brand-green); text-transform: uppercase; line-height: 1;
  }
  .contact {
    position: absolute; left: 610px; top: 92px;
    border-left: 1.5px solid var(--brand-green);
    padding-left: 20px; height: 31px;
    display: flex; flex-direction: column; justify-content: center; gap: 2px;
  }
  .contact-line {
    display: flex; align-items: center; gap: 6px;
    font-size: 13.5px; color: var(--ink); line-height: 15px;
  }
  .contact-line svg { width: 10px; height: 10px; flex: none; }
  .watermark {
    position: absolute; left: 160px; top: 300px;
    width: 520px; height: 620px; border-radius: 50%;
    background: radial-gradient(ellipse at center, var(--watermark) 0%, rgba(160,160,160,0.05) 60%, rgba(160,160,160,0) 75%);
  }
  .footer-rule {
    position: absolute; left: 0; width: 855px; height: 3px;
    background: var(--brand-green);
  }
  .footer-rule.top { top: 1029px; }
  .footer-rule.bottom { top: 1164px; }
  .footer-band {
    position: absolute; left: 0; top: 1034px; width: 855px; height: 128px;
    background: var(--earth-brown); color: var(--footer-ink);
    text-align: center; font-size: 13.5px; line-height: 17px;
    padding-top: 25px;
  }
  .directors {
    display: flex; align-items: center; justify-content: center;
    margin-top: 6px;
  }
  .directors::before, .directors::after {
    content: ""; width: 173px; height: 1px; background: var(--footer-ink);
  }
  .directors span { padding: 0 2px; }
  .franchise-note { font-style: italic; margin-top: 7px; }
</style>
</head>
<body>
  <main class="letterhead">
    <header>
      <div class="brand">
        <span class="brand-dot"></span>
        <span class="brand-name">Lofthaven</span>
      </div>
      <div class="contact">
        <div class="contact-line">
          <svg viewBox="0 0 10 10"><path d="M2 0.8 L3.6 2.9 L2.8 3.9 Q4 6.2 6.1 7.2 L7.1 6.4 L9.2 8 L8.2 9.4 Q3.8 9 0.6 1.8 Z" fill="var(--brand-green)"/></svg>
          <span>010 555 0142</span>
        </div>
        <div class="contact-line">
          <svg viewBox="0 0 10 10"><circle cx="5" cy="5" r="4.5" fill="var(--brand-green)"/><path d="M1 5 H9 M5 0.5 Q2.5 5 5 9.5 M5 0.5 Q7.5 5 5 9.5" stroke="#fff" stroke-width="0.7" fill="none"/></svg>
          <span>lofthaven.co.za</span>
        </div>
      </div>
    </header>

    <div class="watermark" role="img" aria-label="Faint brand emblem watermark"></div>

    <footer>
      <div class="footer-rule top"></div>
      <div class="footer-band">
        <p>Highveld Homes (Pty) Ltd t/a Lofthaven Midrand/Kyalami, Reg No: 2023/458812/07</p>
        <p>Unit 12B, Waterfall Square, Corner Kestrel Avenue &amp; Heron Road, Midrand, South Africa</p>
        <p class="directors"><span>Directors: M Venter / LJ Dlamini-Hart</span></p>
        <p class="franchise-note">Each franchise is independently owned &amp; operated</p>
      </div>
      <div class="footer-rule bottom"></div>
    </footer>
  </main>
</body>
</html>
```